Business Card Design

redesign of card and recreation of logo based on image provided. the business is located in new york so the Brooklyn Bridge figures prominently in the scheme. product should be very clean.

Industry/Entity Type

Real Estate

Contact Information for Business Card

Wendell Ortwick 318 Tamsin Street Brooklyn, New York 11409 wendell@qorvane.com Mobile: 917-555-0143

Colors
cadf82
1b1b1b
ffffff

Requirements
Nice to have
• Brooklyn Bridge

```html
<!DOCTYPE html>
<html lang="en">
<head>
<meta charset="utf-8">
<title>Ortwick &amp; Assoc. – Business Card</title>
<link href="https://fonts.googleapis.com/css2?family=Questrial&display=swap" rel="stylesheet">
<style>
  :root {
    --stage: #1b1b1b;
    --card-dark-top: #4a4a4a;
    --card-dark-bottom: #2c2c2c;
    --card-light: #ffffff;
    --ink: #1b1b1b;
    --ink-light: #e6e6e6;
    --accent: #cadf82;
    --accent-deep: #9fb84a;
  }
  * { box-sizing: border-box; margin: 0; padding: 0; }
  html, body {
    width: 1200px; height: 900px; overflow: hidden;
    background: radial-gradient(ellipse at 50% 45%, #2a2a2a 0%, var(--stage) 70%);
    font-family: "Questrial", "Century Gothic", sans-serif;
  }
  .canvas { position: relative; width: 1200px; height: 900px; }
  .card {
    position: absolute; width: 560px; height: 320px; border-radius: 22px;
  }
  .card--back {
    left: 120px; top: 100px;
    background: linear-gradient(160deg, var(--card-dark-top), var(--card-dark-bottom));
    display: flex; flex-direction: column; align-items: center; justify-content: center;
  }
  .card--front {
    left: 520px; top: 480px;
    background: var(--card-light);
  }
  .wordmark {
    display: flex; align-items: center; gap: 12px;
    font-size: 34px; font-weight: 400; letter-spacing: 0.5px; white-space: nowrap;
  }
  .wordmark__square { width: 18px; height: 18px; background: var(--accent); flex: none; }
  .card--back .wordmark__name { color: var(--ink-light); }
  .website {
    margin-top: 44px; color: var(--accent); font-size: 18px; letter-spacing: 1px;
  }
  .card--front .wordmark {
    position: absolute; left: 36px; top: 166px; font-size: 24px; gap: 10px;
  }
  .card--front .wordmark__square { width: 15px; height: 15px; }
  .card--front .wordmark__name { color: var(--ink); }
  .contact {
    position: absolute; left: 306px; top: 66px; color: var(--ink);
  }
  .contact__name { font-size: 26px; font-weight: 400; line-height: 1; white-space: nowrap; }
  .contact__title {
    font-size: 16px; color: var(--accent-deep); letter-spacing: 2px; margin: 8px 0 14px 14px;
  }
  .contact__list { list-style: none; margin-left: 14px; }
  .contact__item {
    display: flex; align-items: flex-start; gap: 10px;
    font-size: 16px; line-height: 24px; letter-spacing: 0.5px; white-space: nowrap;
  }
  .contact__icon { width: 16px; height: 24px; flex: none; fill: var(--accent-deep); }
</style>
</head>
<body>
<main class="canvas">
  <section class="card card--back" aria-label="Card back">
    <div class="wordmark">
      <span class="wordmark__square"></span>
      <span class="wordmark__name">Ortwick &amp; Assoc.</span>
    </div>
    <p class="website">www.qorvane.com</p>
  </section>

  <section class="card card--front" aria-label="Card front">
    <div class="wordmark">
      <span class="wordmark__square"></span>
      <span class="wordmark__name">Ortwick &amp; Assoc.</span>
    </div>
    <div class="contact">
      <h1 class="contact__name">Wendell Ortwick</h1>
      <p class="contact__title">BROKER</p>
      <ul class="contact__list">
        <li class="contact__item">
          <svg class="contact__icon" viewBox="0 0 16 24"><path d="M4 4h8a1 1 0 0 1 1 1v15a1 1 0 0 1-1 1H4a1 1 0 0 1-1-1V5a1 1 0 0 1 1-1zm1 2v11h6V6zm3 12.2a.9.9 0 1 0 0 1.8.9.9 0 0 0 0-1.8z"/></svg>
          917 555 0143
        </li>
        <li class="contact__item">
          <svg class="contact__icon" viewBox="0 0 16 24"><path d="M1 8h14v1L8 13 1 9zm0 2.5 7 4 7-4V17H1z"/></svg>
          wendell@qorvane.com
        </li>
        <li class="contact__item">
          <svg class="contact__icon" viewBox="0 0 16 24"><path d="M8 5a5 5 0 0 1 5 5c0 4-5 10-5 10S3 14 3 10a5 5 0 0 1 5-5zm0 3a2 2 0 1 0 0 4 2 2 0 0 0 0-4z"/></svg>
          <span>318 Tamsin Street<br>Brooklyn, NY 11409</span>
        </li>
      </ul>
    </div>
  </section>
</main>
</body>
</html>
```